Internal Web Pages for Metrivane Labs

I need internal web pages (Why Metrivane Labs?, What We Offer, Blog, Testimonials) that match the design of the homepage. These do not need to be as long or in-depth as the landing page (provided for reference) but I will need three, maybe four, total pages (I'll select the max number of pages for now, but these will all be simple and short pages). Also attached is our new logo design for the company.

They are to essentially be:
Why Metrivane Labs? - An About Us and Why Choose Us page rolled into one.
What We Offer - A Services type page
Blog - self-explanatory
Testimonials - Customer Reviews and Use Cases

Also, maybe a very simple "Contact Us" page as well.

Target Market(s)

Business professionals that work with data analytics teams

Industry/Entity Type

Data Science

Number of Pages Required

5+ page

Requirements
Must have
• It must match the original design in theme and colors.
Nice to have
• Simple pages that show continuity that flows from the original landing page.
Should not have
• Can not be a different design that does not match the landing page.

```html
<!DOCTYPE html>
<html lang="en">
<head>
<meta charset="utf-8">
<title>Blog | Metrivane Labs</title>
<link href="https://fonts.googleapis.com/css2?family=Poppins:wght@300;400;500;600&family=Roboto:ital,wght@0,400;0,500;0,700;1,500&family=Merriweather:wght@300&display=swap" rel="stylesheet">
<style>
:root{
  --brand:#5a5fe0;
  --brand-dark:#4c4fc9;
  --orange:#f7890b;
  --ink:#1d1d2b;
  --text:#3e3e4a;
  --muted:#6b6b78;
  --line:#e1e1ea;
  --footer:#1c0a47;
  --footer-bottom:#140536;
  --white:#ffffff;
}
*{margin:0;padding:0;box-sizing:border-box}
html,body{width:1200px;height:2682px;overflow:hidden;background:var(--white)}
body{position:relative;font-family:'Roboto',sans-serif;color:var(--text)}
.abs{position:absolute}

/* header */
.site-header{position:absolute;left:0;top:0;width:1200px;height:87px;background:var(--white)}
.brand{position:absolute;display:flex;align-items:center;gap:10px;font-family:'Poppins',sans-serif;font-weight:300;color:var(--brand)}
.brand-mark{width:30px;height:30px;background:var(--brand);border-radius:4px}
.site-header .brand{left:117px;top:20px;font-size:38px}
.main-nav{position:absolute;left:469px;top:29px;display:flex;gap:32px;font-family:'Poppins',sans-serif;font-size:18px;font-weight:300;color:#33333f}
.main-nav .active{color:var(--brand)}
.btn-cta{position:absolute;left:977px;top:23px;width:132px;height:39px;background:var(--orange);color:#fff;font-family:'Poppins',sans-serif;font-weight:600;font-size:14px;letter-spacing:.5px;display:flex;align-items:center;justify-content:center;box-shadow:0 4px 10px rgba(247,137,11,.35)}

/* hero */
.hero{position:absolute;left:0;top:87px;width:1200px;height:410px}
.hero svg{position:absolute;left:0;top:0}
.hero-title{position:absolute;left:121px;top:140px;font-family:'Poppins',sans-serif;font-weight:300;font-size:40px;color:#fff}

/* section head */
.section-title{position:absolute;left:0;top:568px;width:1200px;text-align:center;font-family:'Poppins',sans-serif;font-weight:400;font-size:40px;color:var(--ink)}
.section-rule{position:absolute;left:529px;top:628px;width:142px;height:2px;background:var(--brand)}

/* date badge */
.date-badge{position:absolute;width:46px;height:46px;border-radius:50%;background:var(--brand);color:#fff;font-family:'Poppins',sans-serif;font-weight:600;font-size:11px;line-height:12px;text-align:center;display:flex;align-items:center;justify-content:center;flex-direction:column}

/* featured */
.featured-photo{position:absolute;left:143px;top:686px;width:503px;height:422px;border-radius:14px;background:radial-gradient(ellipse at 45% 45%,#2d4a6a 0%,#0f1e33 55%,#070b14 100%)}
.featured-card{position:absolute;left:574px;top:725px;width:471px;height:346px;background:#fff;border:2px solid var(--line);border-radius:10px;padding:42px 38px 0 39px}
.featured-card h2{font-family:'Roboto',sans-serif;font-weight:700;font-size:16px;line-height:21px;color:var(--ink);text-transform:uppercase}
.featured-card p{font-family:'Merriweather',serif;font-weight:300;font-size:13px;line-height:21.5px;color:#3a3a44;margin:14px 0 0 5px}

.meta{display:flex;align-items:center;gap:20px;font-style:italic;font-weight:500;font-size:14px;color:var(--text);margin-top:14px}
.meta span{display:flex;align-items:center;gap:7px}
.btn-more{display:inline-flex;align-items:center;gap:6px;height:39px;padding:0 20px;border:2px solid var(--brand);border-radius:20px;color:var(--brand);font-family:'Poppins',sans-serif;font-weight:600;font-size:12px;background:#fff}

.featured-card .btn-more{margin-top:16px;width:137px}

/* grid */
.post{position:absolute;width:287px;height:448px}
.post-photo{position:absolute;left:0;top:0;width:287px;height:248px}
.post-card{position:absolute;left:11px;top:183px;width:265px;height:265px;background:#fff;border:2px solid var(--line);border-radius:6px;padding:28px 22px 0 23px}
.post-card h3{font-family:'Roboto',sans-serif;font-weight:700;font-size:14.5px;line-height:21px;color:var(--ink);text-transform:uppercase}
.post-card .meta{margin-top:10px;font-size:14px}
.post-card p{font-size:15.5px;line-height:21.5px;color:#45454f;margin-top:10px}
.post-card .btn-more{margin-top:15px;width:137px;padding:0 22px}
.post .date-badge{left:225px;top:13px}

/* footer */
.site-footer{position:absolute;left:0;top:2200px;width:1200px;height:394px;background:var(--footer);color:#fff}
.site-footer .brand{left:143px;top:65px;font-size:40px;color:var(--brand)}
.footer-about{position:absolute;left:143px;top:141px;width:290px;font-size:16px;line-height:22.5px;color:#e2e0ee}
.socials{position:absolute;left:144px;top:261px;display:flex;gap:8px}
.socials span{width:35px;height:35px;border:1.5px solid #e2e0ee;border-radius:50%}
.footer-heading{position:absolute;font-family:'Roboto',sans-serif;font-weight:700;font-size:18.5px;letter-spacing:.5px}
.contact-list{position:absolute;left:480px;top:118px;list-style:none}
.contact-list li{position:relative;padding-left:38px;font-weight:500;font-size:16px;line-height:21px;letter-spacing:.6px;margin-bottom:20px}
.contact-list svg{position:absolute;left:0;top:2px}
.signup-text{position:absolute;left:754px;top:110px;width:300px;font-size:14px;line-height:24px;color:#e2e0ee}
.email-input{position:absolute;left:754px;top:179px;width:303px;height:40px;background:#fff;border-radius:2px;padding-left:17px;display:flex;align-items:center;color:#666;font-size:14px}
.btn-subscribe{position:absolute;left:754px;top:235px;width:126px;height:39px;background:var(--orange);color:#fff;font-weight:700;font-size:14px;letter-spacing:.5px;display:flex;align-items:center;justify-content:center}
.footer-bottom{position:absolute;left:0;top:2594px;width:1200px;height:88px;background:var(--footer-bottom);color:#fff;font-weight:500;font-size:15.5px;display:flex;align-items:center;justify-content:center}
</style>
</head>
<body>

<header class="site-header">
  <div class="brand"><span class="brand-mark"></span>Metrivane Labs</div>
  <nav class="main-nav">
    <span class="active">Home</span><span>About us</span><span>Our Service</span><span>Blog</span><span>Contact</span>
  </nav>
  <div class="btn-cta">GET STARTED</div>
</header>

<section class="hero">
  <svg width="1200" height="410" viewBox="0 0 1200 410">
    <defs>
      <linearGradient id="heroFill" x1="0" y1="0" x2="1" y2="0.4">
        <stop offset="0" stop-color="#5a4a3c"/>
        <stop offset="0.35" stop-color="#3c4a63"/>
        <stop offset="0.65" stop-color="#4a3f78"/>
        <stop offset="1" stop-color="#231a55"/>
      </linearGradient>
    </defs>
    <polygon points="0,298 411,408 1200,293 1200,308 411,388 140,330" fill="var(--brand)"/>
    <polygon points="0,0 1200,0 1200,293 411,392 0,298" fill="url(#heroFill)" role="img" aria-label="Photo of hands typing on a laptop with glowing data charts and network lines"/>
  </svg>
  <h1 class="hero-title">Latest Blogs</h1>
</section>

<h2 class="section-title">Our Blog Posts</h2>
<div class="section-rule"></div>

<div class="featured-photo" role="img" aria-label="Photo of a hand holding a glowing tablet with analytics dashboards"></div>
<div class="date-badge" style="left:160px;top:711px">OCT<br>2021</div>
<article class="featured-card">
  <h2>Lorem Ipsum is simply dummy text of the printing and typesetting industry.</h2>
  <div class="meta">
    <span><svg width="15" height="13" viewBox="0 0 15 13"><path d="M7.5 1C3.9 1 1 3.2 1 5.9c0 1.4.8 2.6 2 3.5L2.5 12l3-1.6c.6.2 1.3.2 2 .2 3.6 0 6.5-2.2 6.5-4.8S11.1 1 7.5 1z" fill="none" stroke="var(--brand)" stroke-width="1.3"/></svg>2 comments</span>
    <span><svg width="13" height="14" viewBox="0 0 13 14"><circle cx="6.5" cy="4" r="3.2" fill="var(--brand)"/><path d="M0.5 14c0-3.5 2.7-5.5 6-5.5s6 2 6 5.5z" fill="var(--brand)"/></svg>by Mara</span>
  </div>
  <p>Lorem Ipsum is simply dummy text of the printing and typesetting industry. Lorem Ipsum has been the industry's standard dummy text ever since the 1500s, when an unknown printer took a galley of type and scrambled it to make a type specimen book. It has survived not only five centuries, but also the leap into electronic typesetting, remaining essentially</p>
  <span class="btn-more">LERN MORE <svg width="11" height="11" viewBox="0 0 11 11"><path d="M1 5.5h7M5 1.8l4 3.7-4 3.7" fill="none" stroke="var(--brand)" stroke-width="2"/></svg></span>
</article>

<!-- post grid -->
<article class="post" style="left:145px;top:1190px">
  <div class="post-photo" style="background:linear-gradient(135deg,#c9d4e4,#8a96ab 60%,#4c5466)" role="img" aria-label="Photo of two colleagues reviewing charts on a large display wall"></div>
  <div class="date-badge">OCT<br>2021</div>
  <div class="post-card">
    <h3>Nemo enim ipsam volupta quia voluptas sit</h3>
    <div class="meta"><span><svg width="15" height="13" viewBox="0 0 15 13"><path d="M7.5 1C3.9 1 1 3.2 1 5.9c0 1.4.8 2.6 2 3.5L2.5 12l3-1.6c.6.2 1.3.2 2 .2 3.6 0 6.5-2.2 6.5-4.8S11.1 1 7.5 1z" fill="none" stroke="var(--brand)" stroke-width="1.3"/></svg>2 comments</span><span><svg width="13" height="14" viewBox="0 0 13 14"><circle cx="6.5" cy="4" r="3.2" fill="var(--brand)"/><path d="M0.5 14c0-3.5 2.7-5.5 6-5.5s6 2 6 5.5z" fill="var(--brand)"/></svg>by Mara</span></div>
    <p>Sed ut perspiciatis unde omnis iste natus error sit voluptatem accustium dlorue laum</p>
    <span class="btn-more">LERN MORE <svg width="11" height="11" viewBox="0 0 11 11"><path d="M1 5.5h7M5 1.8l4 3.7-4 3.7" fill="none" stroke="var(--brand)" stroke-width="2"/></svg></span>
  </div>
</article>

<article class="post" style="left:456px;top:1190px">
  <div class="post-photo" style="background:linear-gradient(135deg,#2a2622,#4a3f35 50%,#1c2a2a)" role="img" aria-label="Photo of an analyst at a screen of data visualisations"></div>
  <div class="date-badge">OCT<br>2021</div>
  <div class="post-card">
    <h3>Nemo enim ipsam volupta quia voluptas sit</h3>
    <div class="meta"><span><svg width="15" height="13" viewBox="0 0 15 13"><path d="M7.5 1C3.9 1 1 3.2 1 5.9c0 1.4.8 2.6 2 3.5L2.5 12l3-1.6c.6.2 1.3.2 2 .2 3.6 0 6.5-2.2 6.5-4.8S11.1 1 7.5 1z" fill="none" stroke="var(--brand)" stroke-width="1.3"/></svg>2 comments</span><span><svg width="13" height="14" viewBox="0 0 13 14"><circle cx="6.5" cy="4" r="3.2" fill="var(--brand)"/><path d="M0.5 14c0-3.5 2.7-5.5 6-5.5s6 2 6 5.5z" fill="var(--brand)"/></svg>by Mara</span></div>
    <p>Sed ut perspiciatis unde omnis iste natus error sit voluptatem accustium dlorue laum</p>
    <span class="btn-more">LERN MORE <svg width="11" height="11" viewBox="0 0 11 11"><path d="M1 5.5h7M5 1.8l4 3.7-4 3.7" fill="none" stroke="var(--brand)" stroke-width="2"/></svg></span>
  </div>
</article>

<article class="post" style="left:769px;top:1190px">
  <div class="post-photo" style="background:linear-gradient(160deg,#123a5a,#1a6f9a 55%,#0b2540)" role="img" aria-label="Photo of a hand touching glowing holographic bar charts"></div>
  <div class="date-badge">OCT<br>2021</div>
  <div class="post-card">
    <h3>Nemo enim ipsam volupta quia voluptas sit</h3>
    <div class="meta"><span><svg width="15" height="13" viewBox="0 0 15 13"><path d="M7.5 1C3.9 1 1 3.2 1 5.9c0 1.4.8 2.6 2 3.5L2.5 12l3-1.6c.6.2 1.3.2 2 .2 3.6 0 6.5-2.2 6.5-4.8S11.1 1 7.5 1z" fill="none" stroke="var(--brand)" stroke-width="1.3"/></svg>2 comments</span><span><svg width="13" height="14" viewBox="0 0 13 14"><circle cx="6.5" cy="4" r="3.2" fill="var(--brand)"/><path d="M0.5 14c0-3.5 2.7-5.5 6-5.5s6 2 6 5.5z" fill="var(--brand)"/></svg>by Mara</span></div>
    <p>Sed ut perspiciatis unde omnis iste natus error sit voluptatem accustium dlorue laum</p>
    <span class="btn-more">LERN MORE <svg width="11" height="11" viewBox="0 0 11 11"><path d="M1 5.5h7M5 1.8l4 3.7-4 3.7" fill="none" stroke="var(--brand)" stroke-width="2"/></svg></span>
  </div>
</article>

<article class="post" style="left:143px;top:1684px">
  <div class="post-photo" style="background:linear-gradient(150deg,#dfe4ea,#6f7f98 45%,#1f3560)" role="img" aria-label="Photo of a laptop showing blue trading charts and a world map"></div>
  <div class="date-badge">OCT<br>2021</div>
  <div class="post-card">
    <h3>Nemo enim ipsam volupta quia voluptas sit</h3>
    <div class="meta"><span><svg width="15" height="13" viewBox="0 0 15 13"><path d="M7.5 1C3.9 1 1 3.2 1 5.9c0 1.4.8 2.6 2 3.5L2.5 12l3-1.6c.6.2 1.3.2 2 .2 3.6 0 6.5-2.2 6.5-4.8S11.1 1 7.5 1z" fill="none" stroke="var(--brand)" stroke-width="1.3"/></svg>2 comments</span><span><svg width="13" height="14" viewBox="0 0 13 14"><circle cx="6.5" cy="4" r="3.2" fill="var(--brand)"/><path d="M0.5 14c0-3.5 2.7-5.5 6-5.5s6 2 6 5.5z" fill="var(--brand)"/></svg>by Mara</span></div>
    <p>Sed ut perspiciatis unde omnis iste natus error sit voluptatem accustium dlorue laum</p>
    <span class="btn-more">LERN MORE <svg width="11" height="11" viewBox="0 0 11 11"><path d="M1 5.5h7M5 1.8l4 3.7-4 3.7" fill="none" stroke="var(--brand)" stroke-width="2"/></svg></span>
  </div>
</article>

<article class="post" style="left:454px;top:1684px">
  <div class="post-photo" style="background:linear-gradient(160deg,#3a4450,#7fa3c4 50%,#2d3a46)" role="img" aria-label="Photo of a laptop displaying an analysis dashboard beside a plant"></div>
  <div class="date-badge">OCT<br>2021</div>
  <div class="post-card">
    <h3>Nemo enim ipsam volupta quia voluptas sit</h3>
    <div class="meta"><span><svg width="15" height="13" viewBox="0 0 15 13"><path d="M7.5 1C3.9 1 1 3.2 1 5.9c0 1.4.8 2.6 2 3.5L2.5 12l3-1.6c.6.2 1.3.2 2 .2 3.6 0 6.5-2.2 6.5-4.8S11.1 1 7.5 1z" fill="none" stroke="var(--brand)" stroke-width="1.3"/></svg>2 comments</span><span><svg width="13" height="14" viewBox="0 0 13 14"><circle cx="6.5" cy="4" r="3.2" fill="var(--brand)"/><path d="M0.5 14c0-3.5 2.7-5.5 6-5.5s6 2 6 5.5z" fill="var(--brand)"/></svg>by Mara</span></div>
    <p>Sed ut perspiciatis unde omnis iste natus error sit voluptatem accustium dlorue laum</p>
    <span class="btn-more">LERN MORE <svg width="11" height="11" viewBox="0 0 11 11"><path d="M1 5.5h7M5 1.8l4 3.7-4 3.7" fill="none" stroke="var(--brand)" stroke-width="2"/></svg></span>
  </div>
</article>

<article class="post" style="left:766px;top:1684px">
  <div class="post-photo" style="background:linear-gradient(160deg,#1a2a3a,#2e4a5c 50%,#0e1620)" role="img" aria-label="Photo of hands holding a hexagon grid of data icons"></div>
  <div class="date-badge">OCT<br>2021</div>
  <div class="post-card">
    <h3>Nemo enim ipsam volupta quia voluptas sit</h3>
    <div class="meta"><span><svg width="15" height="13" viewBox="0 0 15 13"><path d="M7.5 1C3.9 1 1 3.2 1 5.9c0 1.4.8 2.6 2 3.5L2.5 12l3-1.6c.6.2 1.3.2 2 .2 3.6 0 6.5-2.2 6.5-4.8S11.1 1 7.5 1z" fill="none" stroke="var(--brand)" stroke-width="1.3"/></svg>2 comments</span><span><svg width="13" height="14" viewBox="0 0 13 14"><circle cx="6.5" cy="4" r="3.2" fill="var(--brand)"/><path d="M0.5 14c0-3.5 2.7-5.5 6-5.5s6 2 6 5.5z" fill="var(--brand)"/></svg>by Mara</span></div>
    <p>Sed ut perspiciatis unde omnis iste natus error sit voluptatem accustium dlorue laum</p>
    <span class="btn-more">LERN MORE <svg width="11" height="11" viewBox="0 0 11 11"><path d="M1 5.5h7M5 1.8l4 3.7-4 3.7" fill="none" stroke="var(--brand)" stroke-width="2"/></svg></span>
  </div>
</article>

<footer class="site-footer">
  <div class="brand"><span class="brand-mark"></span>Metrivane Labs</div>
  <p class="footer-about">Sed ut perspiciatis unde omnis iste natus error sit voluptatem accusantium dolorque laudantium, totam rem aperiam, eaque ipsa quae ab illo inventore veritatis et quasi</p>
  <div class="socials"><span></span><span></span><span></span><span></span></div>

  <h4 class="footer-heading" style="left:480px;top:69px">CONTACT US</h4>
  <ul class="contact-list">
    <li><svg width="18" height="22" viewBox="0 0 18 22"><path d="M9 1C5 1 2 4 2 8c0 5 7 13 7 13s7-8 7-13c0-4-3-7-7-7z" fill="none" stroke="#fff" stroke-width="1.4"/><circle cx="9" cy="8" r="2.5" fill="none" stroke="#fff" stroke-width="1.4"/></svg>Metrivane Labs<br>250 ipsam voluptatem<br>quia voluptas</li>
    <li style="margin-top:28px"><svg width="20" height="20" viewBox="0 0 20 20"><path d="M4 1.5l3 4-2 2.5c1.3 2.7 3.3 4.7 6 6l2.5-2 4 3-1.5 3.5C9 18 2 11 0.8 3.5z" fill="none" stroke="#fff" stroke-width="1.3"/></svg>Phone :<br>404-7100-3300</li>
    <li style="margin-top:28px"><svg width="21" height="15" viewBox="0 0 21 15"><rect x="1" y="1" width="19" height="13" fill="none" stroke="#fff" stroke-width="1.3"/><path d="M1 1l9.5 8L20 1" fill="none" stroke="#fff" stroke-width="1.3"/></svg>Email :<br>hello@metrivanelabs.com</li>
  </ul>

  <h4 class="footer-heading" style="left:754px;top:66px">SIGN UP TO RECEIVE EMAIL</h4>
  <p class="signup-text">Excepteur sint occaecat cupidatat non proident, sunt in culpa qui Nemo enim ipsam vo-</p>
  <div class="email-input">Enter Email</div>
  <div class="btn-subscribe">SUBSCRIBE</div>
</footer>
<div class="footer-bottom">Copyright © Metrivane Labs 2021. All rights reserved. | Privacy Policy</div>

</body>
</html>
```